Business Card Design Project

We are a distribution company providing goods to Latin America. We sell everything from Medical equipment, generic medicines, to carecliners. The logo that we use is attached. The logo can incorporate different colors other than black for versatility. The company name is Valdoria International Corporation and/or VIC. The card will be printed using 1 or more of the following: Silk mounted and/or embossed. So if the design ideas could be made to incorporate that technique or any other unique techniques, it would be great. The target market is dialysis centers/doctors.

Basic Info for card:
Marnie Dowsett
Purchasing Manager
555-317-4086 direct
555-241-7953 fax
marnie.dowsett@valdoriavic.example
www.valdoriavic.example

Target Market(s)

Latin America

Industry/Entity Type

Business

Requirements
Nice to have
• The Front of the card should have the basic contact information with company name/logo. The back of the card could incorporate

```html
<!DOCTYPE html>
<html lang="en">
<head>
<meta charset="utf-8">
<title>Valdoria International Corporation – Business Card</title>
<link rel="stylesheet" href="https://fonts.googleapis.com/css2?family=Open+Sans:wght@300;400&display=swap">
<style>
  :root {
    --backdrop: #000000;
    --card: #ffffff;
    --ink-strong: #1e1e1e;
    --ink-soft: #8a8a8a;
    --mark: #111111;
  }
  html, body {
    margin: 0;
    padding: 0;
    width: 1200px;
    height: 900px;
    overflow: hidden;
    background: var(--backdrop);
  }
  .canvas {
    position: relative;
    width: 1200px;
    height: 900px;
    background: var(--backdrop);
    font-family: "Open Sans", sans-serif;
  }
  .card {
    position: absolute;
    left: 259px;
    top: 231px;
    width: 684px;
    height: 360px;
    background: var(--card);
  }
  .contact {
    position: absolute;
    left: 33px;
    top: 24px;
    margin: 0;
    font-size: 17px;
    line-height: 22px;
    font-weight: 300;
    color: var(--ink-soft);
  }
  .contact p { margin: 0; }
  .contact .person-name {
    color: var(--ink-strong);
    font-weight: 400;
  }
  .contact .group { margin-top: 22px; }
  .brand-mark {
    position: absolute;
    right: 34px;
    top: 196px;
    display: flex;
    align-items: center;
    gap: 12px;
    font-size: 34px;
    font-weight: 400;
    letter-spacing: 2px;
    color: var(--mark);
  }
  .brand-mark .dot {
    width: 18px;
    height: 18px;
    border-radius: 50%;
    background: var(--mark);
  }
  .company-name {
    position: absolute;
    right: 30px;
    top: 299px;
    margin: 0;
    font-size: 18px;
    font-weight: 300;
    color: var(--ink-soft);
    letter-spacing: 0.2px;
  }
</style>
</head>
<body>
<div class="canvas">
  <section class="card">
    <div class="contact">
      <p class="person-name">Marnie Dowsett</p>
      <p class="job-title">Purchasing Manager</p>
      <div class="group phones">
        <p>555-317-4086 direct</p>
        <p>555-241-7953 fax</p>
      </div>
      <div class="group web">
        <p>marnie.dowsett@valdoriavic.example</p>
        <p>www.valdoriavic.example</p>
      </div>
    </div>
    <div class="brand-mark"><span class="dot"></span><span>VIC</span></div>
    <p class="company-name">Valdoria International Corporation</p>
  </section>
</div>
</body>
</html>
```